I need a new business card design for my pharmacy.

I need a business card design. I will include my logo.
The card needs to be readable. I prefer to have my logo on one side along with my website, the other side includes the other information. Please use combination of black, neon green, white, and silver. This needs to catch the eye but yet be clearly visible and legible. Thanks

Industry/Entity Type

Pharmacy

Contact Information for Business Card

It needs to have the following information listed:
Mel's Apothecary Owner/Pharm D.
7134 North Brook Lane
Sioux Falls, SD 57231
Phone 605-318-6207
Fax 605-318-6209
email: mel@melsapothecary-example.com
www.melsapothecary-example.com
Store hours Monday-Friday 8 am- 7 pm
Saturday 8 am- 12 pm
Sunday Closed
Please utilize the colors black, white, and neon green, maybe silver.

Requirements
Must have
• It needs to be easily readable!
Nice to have
• It should catch the eye.
Should not have
• Do not use any other colors except listed: black, neon green, white, & silver.

```html
<!DOCTYPE html>
<html lang="en">
<head>
<meta charset="utf-8">
<title>Mel's Apothecary – Business Card Front</title>
<link rel="stylesheet" href="https://fonts.googleapis.com/css2?family=Hind:wght@600&family=Montserrat:wght@600&display=swap">
<style>
  :root {
    --neon-green: #0bd40b;
    --neon-green-bright: #22f522;
    --neon-green-deep: #00c400;
    --black: #0a0a0a;
    --white: #ffffff;
    --silver-light: #f2f2f2;
    --silver: #d6d6d6;
    --silver-dark: #bdbdbd;
    --stripe-light: rgba(235, 255, 235, 0.55);
    --stripe-silver: rgba(150, 150, 150, 0.35);
  }
  * { box-sizing: border-box; margin: 0; padding: 0; }
  html, body {
    width: 1200px;
    height: 1000px;
    overflow: hidden;
    background: var(--white);
  }
  .canvas {
    position: relative;
    width: 1200px;
    height: 1000px;
  }
  .card {
    position: absolute;
    left: 27px;
    top: 145px;
    width: 1150px;
    height: 710px;
    overflow: hidden;
    background: var(--silver);
  }
  .card__green {
    position: absolute;
    left: 0; top: 0;
    width: 1150px;
    height: 520px;
    background: radial-gradient(ellipse at 45% 35%, var(--neon-green-bright) 0%, var(--neon-green) 55%, var(--neon-green-deep) 100%);
  }
  .card__stripes {
    position: absolute;
    left: 0; top: 0;
    width: 338px;
    height: 520px;
    background: repeating-linear-gradient(
      to bottom,
      transparent 0px, transparent 8px,
      var(--stripe-light) 8px, var(--stripe-light) 11px
    );
  }
  .card__silver {
    position: absolute;
    left: 0; top: 520px;
    width: 1150px;
    height: 190px;
    background: linear-gradient(90deg, var(--silver-dark) 0%, var(--silver-light) 30%, var(--silver) 55%, var(--silver-light) 78%, var(--silver-dark) 100%);
  }
  .card__silver-stripes {
    position: absolute;
    left: 0; top: 520px;
    width: 338px;
    height: 190px;
    background: repeating-linear-gradient(
      to bottom,
      transparent 0px, transparent 8px,
      var(--stripe-silver) 8px, var(--stripe-silver) 10px
    );
  }
  .brand-mark {
    position: absolute;
    left: 48px;
    top: 255px;
    width: 260px;
    display: flex;
    align-items: center;
    gap: 14px;
  }
  .brand-mark__dot {
    flex: none;
    width: 34px;
    height: 34px;
    border-radius: 50%;
    background: var(--black);
  }
  .brand-mark__name {
    font-family: "Hind", sans-serif;
    font-weight: 600;
    font-size: 36px;
    line-height: 1;
    color: var(--black);
  }
  .divider {
    position: absolute;
    left: 336px;
    top: 228px;
    width: 3px;
    height: 200px;
    background: var(--black);
  }
  .business-name {
    position: absolute;
    left: 393px;
    top: 268px;
    width: 720px;
    font-family: "Hind", sans-serif;
    font-weight: 600;
    font-size: 84px;
    line-height: 1;
    letter-spacing: -1px;
    color: var(--black);
    white-space: nowrap;
  }
  .website {
    position: absolute;
    left: 393px;
    top: 446px;
    width: 700px;
    text-align: center;
    font-family: "Montserrat", sans-serif;
    font-weight: 600;
    font-size: 31px;
    line-height: 1;
    color: var(--white);
    white-space: nowrap;
  }
</style>
</head>
<body>
  <div class="canvas">
    <div class="card">
      <div class="card__green"></div>
      <div class="card__stripes"></div>
      <div class="card__silver"></div>
      <div class="card__silver-stripes"></div>

      <div class="brand-mark">
        <span class="brand-mark__dot"></span>
        <span class="brand-mark__name">Mel's<br>Apothecary</span>
      </div>

      <div class="divider"></div>

      <h1 class="business-name">Mel's Apothecary</h1>
      <p class="website">www.melsapothecary-example.com</p>
    </div>
  </div>
</body>
</html>
```